We need a postcard design for a new promotion. We are an Australian online store that sells craft mosaic supplies, mainly tiles. View our website to understand more about our product range, www.brightpebbleworks.com.au and what we are about.

This promotion is designed to be used with mosaic studios / classes, as a referral system. They will give these cards to their students who will use them when placing an order. They will enter the studios / classes name during the checkout process. The studio will then receive a credit which will entitle them to receive mosaic supplies.

Target Market(s)

Women aged between 30-65, interest in art & craft

Industry/Entity Type

Store

Requirements
Must have
• Logo
Phone number: 1300 584 716
Website URL: www.brightpebbleworks.com.au

The following wording:

You Can Help Stock Your Studio...
Simply place any order with The Pebble Works and we will give your studio mosaic supplies, to the value of 10% of your purchase.

Just enter your studios name in the comments box during checkout to ensure your studio receives their supplies.

Studio Name:

```html
<!DOCTYPE html>
<html lang="en">
<head>
<meta charset="utf-8">
<title>The Pebble Works – Studio Referral Postcard</title>
<link href="https://fonts.googleapis.com/css2?family=Arimo:wght@400;500;600&display=swap" rel="stylesheet">
<style>
  :root {
    --paper: #ffffff;
    --headline: #5ddfe6;
    --body-text: #8c95e0;
    --contact: #9aa6b2;
    --brand: #7f8a86;
    --brand-square: #5ad1c8;
    --tone-aqua: #a8f5e6;
    --tone-teal: #6fd3c3;
    --tone-blue: #9aa6ee;
    --tone-pink: #fd8ccc;
    --tone-blush: #ffb3d6;
  }
  html, body {
    margin: 0;
    padding: 0;
    overflow: hidden;
    background: var(--paper);
  }
  .postcard {
    position: relative;
    width: 1200px;
    height: 930px;
    background: var(--paper);
    overflow: hidden;
    font-family: "Arimo", Arial, sans-serif;
  }
  .feature-art {
    position: absolute;
    left: 33px;
    top: 33px;
    width: 510px;
    height: 641px;
    background:
      radial-gradient(circle at 75% 40%, rgba(111, 211, 195, 0.55), rgba(111, 211, 195, 0) 45%),
      linear-gradient(180deg,
        var(--tone-aqua) 0%,
        var(--tone-teal) 35%,
        var(--tone-blue) 55%,
        var(--tone-pink) 78%,
        var(--tone-blush) 100%);
  }
  .headline-panel {
    position: absolute;
    left: 98px;
    top: 251px;
    width: 349px;
    height: 94px;
    background: rgba(255, 255, 255, 0.72);
    box-sizing: border-box;
    padding: 1px 0 0 3px;
  }
  .headline {
    margin: 0;
    font-weight: 500;
    font-size: 33px;
    line-height: 46px;
    color: var(--headline);
    white-space: nowrap;
  }
  .offer {
    position: absolute;
    left: 801px;
    top: 188px;
    width: 390px;
    color: var(--body-text);
    font-size: 25.5px;
    line-height: 36px;
    white-space: nowrap;
  }
  .offer p { margin: 0 0 35px 0; }
  .studio-name { font-weight: 600; }
  .brand {
    position: absolute;
    left: 62px;
    top: 722px;
    display: flex;
    align-items: center;
    gap: 12px;
  }
  .brand-mark {
    width: 44px;
    height: 44px;
    background: var(--brand-square);
  }
  .brand-name {
    font-size: 26px;
    color: var(--brand);
    letter-spacing: 0.5px;
  }
  .contact {
    position: absolute;
    left: 139px;
    top: 806px;
    color: var(--contact);
    font-size: 21.5px;
    line-height: 29px;
    font-style: normal;
  }
  .contact p { margin: 0; }
</style>
</head>
<body>
<main class="postcard">
  <div class="feature-art" role="img" aria-label="Cluster of overlapping translucent mosaic tiles in aqua, teal, blue and pink"></div>

  <div class="headline-panel">
    <h1 class="headline">You Can Help Stock<br>Your Studio...</h1>
  </div>

  <section class="offer">
    <p>Simply place any order with<br>The Pebble Works and we<br>will give your studio mosaic<br>supplies, to the value of 10% of<br>your purchase.</p>
    <p>Just enter your studios name<br>in the comments box during<br>checkout to ensure your studio<br>receives their supplies.</p>
    <p class="studio-name">Studio Name:</p>
  </section>

  <div class="brand">
    <span class="brand-mark"></span>
    <span class="brand-name">The Pebble Works</span>
  </div>

  <address class="contact">
    <p>1300 584 716</p>
    <p>www.brightpebbleworks.com.au</p>
  </address>
</main>
</body>
</html>
```